Income Tax Flyer - Updates Needed

Just need to update this flyer design and give it a new look. We would like to keep all the same wording but make it stand out a little more. Our selling point is the "Same Day Tax Advance up to $6,000"

Industry/Entity Type

Lending, Small Loans, Tax Services, Title Loans, Personal Loans

```html
<!DOCTYPE html>
<html lang="en">
<head>
<meta charset="utf-8">
<title>Ledgerline Financial Group – Easy Advance Flyer</title>
<link href="https://fonts.googleapis.com/css2?family=Roboto:wght@400;500;700;900&family=Roboto+Condensed:wght@400;700&display=swap" rel="stylesheet">
<style>
  :root {
    --backdrop: #4f4f4f;
    --paper: #ffffff;
    --header-grey: #eeeeee;
    --brand-green: #17502f;
    --brand-green-light: #1b7a3e;
    --brand-red: #c8161d;
    --brand-red-dark: #8f1515;
    --ink: #1b1b1b;
    --photo-dark: #07131b;
    --photo-mid: #1d3a52;
    --rule: #2a2a2a;
  }
  * { box-sizing: border-box; margin: 0; padding: 0; }
  html, body {
    width: 973px; height: 1200px; overflow: hidden;
    background: var(--backdrop);
  }
  .flyer {
    position: absolute; left: 135px; top: 56px;
    width: 703px; height: 1087px;
    background: var(--paper);
    overflow: hidden;
    font-family: "Roboto", Arial, sans-serif;
    color: var(--ink);
  }
  .header-wave { position: absolute; left: 0; top: 0; width: 703px; height: 250px; }
  .brand {
    position: absolute; left: 0; top: 150px; width: 703px;
    text-align: center;
    font-family: "Roboto", Arial, sans-serif;
    font-weight: 500; font-size: 30px; letter-spacing: 0.5px;
    color: var(--brand-green);
  }
  .brand-mark {
    display: inline-block; width: 14px; height: 14px; border-radius: 50%;
    background: var(--brand-red); margin-right: 10px; vertical-align: 3px;
  }
  .apply-label {
    position: absolute; left: 159px; top: 283px; width: 386px; height: 45px;
    background: var(--brand-green); border-radius: 3px;
    color: #fff; text-align: center;
    font-family: "Roboto Condensed", Arial, sans-serif;
    font-size: 44px; line-height: 45px; font-weight: 400;
  }
  .apply-shadow {
    position: absolute; left: 185px; top: 330px; width: 334px; height: 8px;
    background: radial-gradient(ellipse at top, rgba(0,0,0,0.3), rgba(0,0,0,0) 70%);
  }
  .amount {
    position: absolute; left: 0; top: 350px; width: 703px;
    text-align: center; color: var(--brand-red);
    font-family: "Roboto Condensed", Arial, sans-serif;
    font-weight: 700; font-size: 50px; line-height: 52px;
  }
  .hero-photo {
    position: absolute; left: 0; top: 430px; width: 703px; height: 330px;
    background: radial-gradient(ellipse at 60% 40%, var(--photo-mid) 0%, #0f2535 50%, var(--photo-dark) 100%);
  }
  .hero-line {
    position: absolute; left: 0; width: 703px; text-align: center;
  }
  .hero-intro {
    top: 642px; color: #fff; font-size: 33px; font-weight: 400;
    font-family: "Roboto Condensed", Arial, sans-serif;
  }
  .hero-offer {
    top: 688px; color: var(--brand-red); font-size: 50px; font-weight: 700;
    font-family: "Roboto Condensed", Arial, sans-serif;
  }
  .steps-line { position: absolute; left: 0; top: 0; width: 703px; height: 1087px; pointer-events: none; }
  .step-box {
    position: absolute; top: 798px; width: 70px; height: 70px;
    background: #fff; border: 1px solid #333; border-radius: 5px;
  }
  .step-box svg { width: 70px; height: 70px; display: block; }
  .step-label {
    position: absolute; top: 882px; width: 160px; text-align: center;
    font-size: 17px; line-height: 21px; color: var(--ink);
  }
  .phone {
    position: absolute; left: 424px; top: 954px;
    font-size: 35px; font-weight: 500; color: var(--ink); letter-spacing: 0.3px;
  }
  .address-label {
    position: absolute; left: 414px; top: 1050px;
    font-size: 8px; letter-spacing: 1px; color: var(--ink);
    transform: rotate(-90deg); transform-origin: left top;
  }
  .address-line {
    position: absolute; left: 442px; width: 205px; height: 1px; background: var(--brand-red);
  }
  .cta {
    position: absolute; left: 0; top: 983px; width: 307px; height: 62px;
    background: linear-gradient(90deg, var(--brand-green) 0%, var(--brand-green-light) 100%);
    border-radius: 0 32px 32px 0;
    color: #fff; font-family: "Roboto Condensed", Arial, sans-serif;
    font-size: 25px; line-height: 62px; padding-left: 33px;
  }
  .cta strong { font-weight: 700; }
  .cta-shadow {
    position: absolute; left: 120px; top: 1046px; width: 190px; height: 7px;
    background: radial-gradient(ellipse at top, rgba(0,0,0,0.25), rgba(0,0,0,0) 70%);
  }
</style>
</head>
<body>
<main class="flyer">
  <svg class="header-wave" viewBox="0 0 703 250" aria-hidden="true">
    <path d="M0 0 H703 V154 Q352 318 0 154 Z" fill="var(--header-grey)"/>
    <path d="M0 154 Q352 318 703 154 L703 164 Q352 320 0 166 Z" fill="var(--brand-red-dark)"/>
  </svg>

  <div class="brand"><span class="brand-mark"></span>Ledgerline Financial Group</div>

  <div class="apply-label">APPLY HERE FOR</div>
  <div class="apply-shadow"></div>
  <div class="amount">$5,000-$6,000 TODAY!</div>

  <div class="hero-photo" role="img" aria-label="Photo of a businessman in a dark blue suit cupping his hands around a glowing dollar sign"></div>
  <div class="hero-line hero-intro">File your taxes and apply for an</div>
  <div class="hero-line hero-offer">EASY ADVANCE</div>

  <svg class="steps-line" viewBox="0 0 703 1087" aria-hidden="true">
    <line x1="57" y1="833" x2="646" y2="833" stroke="var(--rule)" stroke-width="1"/>
    <circle cx="57" cy="833" r="3" fill="var(--rule)"/>
    <circle cx="646" cy="833" r="3" fill="var(--rule)"/>
    <path d="M429 1010 a6 6 0 1 1 12 0 c0 5 -6 11 -6 11 s-6 -6 -6 -11z" fill="none" stroke="var(--ink)" stroke-width="1.6"/>
    <circle cx="435" cy="1010" r="2" fill="var(--ink)"/>
  </svg>

  <div class="step-box" style="left:104px">
    <svg viewBox="0 0 70 70" aria-hidden="true">
      <rect x="31" y="12" width="10" height="5" rx="2" fill="var(--brand-red)"/>
      <circle cx="36" cy="39" r="17" fill="none" stroke="var(--brand-red)" stroke-width="3"/>
      <path d="M48 20 l6 2 -2 6z" fill="var(--brand-red)"/>
      <text x="36" y="46" text-anchor="middle" font-family="Roboto, sans-serif" font-weight="700" font-size="18" fill="var(--brand-red)">$</text>
    </svg>
  </div>
  <div class="step-box" style="left:316px">
    <svg viewBox="0 0 70 70" aria-hidden="true">
      <rect x="16" y="20" width="36" height="20" rx="2" fill="var(--brand-red)" transform="rotate(8 34 30)"/>
      <circle cx="35" cy="31" r="6" fill="#fff"/>
      <text x="35" y="35" text-anchor="middle" font-family="Roboto, sans-serif" font-weight="700" font-size="10" fill="var(--brand-red)">$</text>
      <path d="M44 36 v14 h10 v-8 l-6 -2 v-4 z" fill="#fff" stroke="var(--brand-red)" stroke-width="1.5"/>
    </svg>
  </div>
  <div class="step-box" style="left:529px">
    <svg viewBox="0 0 70 70" aria-hidden="true">
      <path d="M31 16 h8 l-3 5 z" fill="var(--brand-red)"/>
      <circle cx="35" cy="30" r="9" fill="var(--brand-red)"/>
      <text x="35" y="34" text-anchor="middle" font-family="Roboto, sans-serif" font-weight="700" font-size="11" fill="#fff">$</text>
      <path d="M14 52 l8 -8 h14 a2 2 0 0 1 0 4 h-8 M36 48 l14 -6 a2 2 0 0 1 2 3 l-20 12 h-12 l-6 3" fill="none" stroke="var(--brand-red)" stroke-width="1.5" stroke-linejoin="round"/>
    </svg>
  </div>

  <div class="step-label" style="left:62px">Available in<br>24 Hours or Less</div>
  <div class="step-label" style="left:271px">Choose Your<br>Loan Amount</div>
  <div class="step-label" style="left:484px">Quick and<br>Easy</div>

  <div class="phone">+012 555 0147</div>
  <div class="address-label">Address</div>
  <div class="address-line" style="top:1012px"></div>
  <div class="address-line" style="top:1037px"></div>
  <div class="address-line" style="top:1061px"></div>

  <div class="cta">CONTRACT US <strong>TODAY!</strong></div>
  <div class="cta-shadow"></div>
</main>
</body>
</html>
```